Morning Harbor Bible Fellowship needs a new Business Card/Letterhead Suite

***** IT DOES NOT HAVE TO FEATURE GREEN AND BROWN in order to be a successful design*****

****FONTS: SF New Republic, 'Morning Harbor'; Nexa Light, 'Bible Fellowship'****

***We have two locations, with two addresses. So the business card AND letterhead need to include two sets of address information***

We are a growing church in New York in need of a new stationary suite. We have recently adopted a new logo (via a successful ArtHivePro project) and need new business cards, letterhead, envelopes, and folders.

We would like to see creative, original designs that are modern and clean/elegant (NOT dated "churchy" graphics that are cheesy).

We need this project worked on immediately, as we need to print new business cards for upcoming programs we have on our schedule. So, the designs need to be solid so that we can move quickly throughout the revision process toward print.

We'd also need editables files, so that we can drop in other staff members names/phone numbers, to be able to print cards for those staff needing them.

Requirements
Must have
• Our logo
• Must be given to us in an editable format (to change names)
Nice to have
• Some examples on grey, or recycled, card stock
• card stock (background) does not have to be white
Should not have
• Any extraneous logo's or symbols

```html
<!DOCTYPE html>
<html lang="en">
<head>
<meta charset="utf-8">
<title>Morning Harbor Bible Fellowship – Business Card</title>
<link rel="stylesheet" href="https://fonts.googleapis.com/css2?family=Montserrat:wght@300;400;700&display=swap">
<style>
  :root {
    --backdrop: #eef2ef;
    --card-white: #ffffff;
    --card-black: #1d1d1d;
    --brand-green: #4d9a1f;
    --rule-green: #3f7d1a;
    --text-white: #ffffff;
    --text-grey: #c9c9c9;
    --leaf-tone-a: #2e2e2e;
    --leaf-tone-b: #3a3a3a;
  }
  * { margin: 0; padding: 0; box-sizing: border-box; }
  html, body {
    width: 1200px; height: 900px; overflow: hidden;
    background: var(--backdrop);
    font-family: 'Montserrat', Arial, sans-serif;
  }
  .suite {
    width: 1200px; height: 900px;
    display: flex; flex-direction: column;
    align-items: center; justify-content: center; gap: 60px;
  }
  .card {
    position: relative;
    width: 630px; height: 360px;
    box-shadow: 0 10px 28px rgba(0,0,0,0.16);
    overflow: hidden;
  }
  /* Front */
  .card--front {
    background: var(--card-white);
    display: flex; align-items: center; justify-content: center;
  }
  .wordmark { text-align: center; color: var(--brand-green); font-weight: 300; }
  .wordmark__name { font-size: 50px; letter-spacing: -0.5px; line-height: 1; }
  .wordmark__sub { font-size: 16px; letter-spacing: 9px; margin-top: 12px; }
  /* Back */
  .card--back { background: var(--card-black); color: var(--text-white); }
  .leaf-decoration {
    position: absolute; right: 0; top: 0;
    width: 260px; height: 250px;
    background: radial-gradient(ellipse at 70% 35%, var(--leaf-tone-b), var(--leaf-tone-a) 55%, transparent 80%);
  }
  .back-wordmark {
    position: absolute; right: 40px; top: 44px;
    text-align: right; color: var(--brand-green); font-weight: 300;
  }
  .back-wordmark__name { font-size: 26px; line-height: 1; }
  .back-wordmark__sub { font-size: 9px; letter-spacing: 4.5px; margin-top: 6px; }
  .person {
    position: absolute; left: 40px; top: 162px;
    font-weight: 700; font-size: 20px;
  }
  .addresses {
    position: absolute; left: 40px; top: 200px;
    font-size: 11px; line-height: 18px; color: var(--text-grey); font-weight: 400;
  }
  .divider {
    position: absolute; left: 40px; right: 40px; top: 250px;
    height: 1px; background: var(--rule-green);
  }
  .contacts {
    position: absolute; top: 270px; font-size: 12px; color: var(--text-grey);
    display: flex; flex-direction: column; gap: 10px;
  }
  .contacts--phones { left: 40px; }
  .contacts--online { left: 360px; }
  .contact { display: flex; align-items: center; gap: 10px; }
  .contact svg { width: 16px; height: 16px; flex: none; }
</style>
</head>
<body>
<main class="suite">
  <section class="card card--front" aria-label="Business card front">
    <div class="wordmark">
      <div class="wordmark__name">Morning Harbor</div>
      <div class="wordmark__sub">BIBLE FELLOWSHIP</div>
    </div>
  </section>

  <section class="card card--back" aria-label="Business card back">
    <div class="leaf-decoration" role="img" aria-label="Faint leaf motif decoration"></div>
    <div class="back-wordmark">
      <div class="back-wordmark__name">Morning Harbor</div>
      <div class="back-wordmark__sub">BIBLE FELLOWSHIP</div>
    </div>
    <h1 class="person">Daniel Whitcombe, D.Min</h1>
    <p class="addresses">
      Main Campus: 18 Linden Crest Avenue, Harborview, NY 11950<br>
      Ministry Center: 302 Linden Crest Avenue, Harborview, NY 11950
    </p>
    <div class="divider"></div>
    <div class="contacts contacts--phones">
      <div class="contact">
        <svg viewBox="0 0 16 16" aria-hidden="true"><circle cx="8" cy="8" r="7.5" fill="none" stroke="#4d9a1f"/><path d="M5.2 4.6l1.4-.4.8 1.8-.9.7c.4.9 1 1.6 1.9 2l.7-.9 1.8.8-.4 1.4c-2.9.2-5.5-2.5-5.3-5.4z" fill="#4d9a1f"/></svg>
        <span>555-014-2271</span>
      </div>
      <div class="contact">
        <svg viewBox="0 0 16 16" aria-hidden="true"><circle cx="8" cy="8" r="7.5" fill="none" stroke="#4d9a1f"/><rect x="5.5" y="3.8" width="5" height="8.4" rx="1" fill="none" stroke="#4d9a1f"/><circle cx="8" cy="10.8" r=".6" fill="#4d9a1f"/></svg>
        <span>555-014-8836</span>
      </div>
    </div>
    <div class="contacts contacts--online">
      <div class="contact">
        <svg viewBox="0 0 16 16" aria-hidden="true"><circle cx="8" cy="8" r="7.5" fill="none" stroke="#4d9a1f"/><rect x="4" y="5" width="8" height="6" fill="none" stroke="#4d9a1f"/><path d="M4 5l4 3.3L12 5" fill="none" stroke="#4d9a1f"/></svg>
        <span>seniorpastor@mhbf.org</span>
      </div>
      <div class="contact">
        <svg viewBox="0 0 16 16" aria-hidden="true"><circle cx="8" cy="8" r="7.5" fill="none" stroke="#4d9a1f"/><circle cx="8" cy="8" r="4.2" fill="none" stroke="#4d9a1f"/><path d="M3.8 8h8.4M8 3.8c-1.6 2.6-1.6 5.8 0 8.4M8 3.8c1.6 2.6 1.6 5.8 0 8.4" fill="none" stroke="#4d9a1f" stroke-width=".8"/></svg>
        <span>www.mhbf.org</span>
      </div>
    </div>
  </section>
</main>
</body>
</html>
```